GRAPHIC DESIGN FOR RESTAURANT MENU FOR HEALTHY RESTAURANT

I am looking for a graphic design for our menu displayed on a TV screen. Please ensure the file will fit on a TV screen nicely. We are looking for a clean design , with the following items. We would also like to include a couple of photos.
Breakfast:
Protein Chocolate Chip Pancakes - $12.95
Dawn Hustle Burrito- $11.95
Hearty Harvest Omelette - $12.95
Lunch
Butter Chicken - $13.95
Chicken Quesadilla - $13.45
Coconut Garlic Shrimp - $15.95
Goat Cheese Stuffed Chicken - $14.95
Chipotle Steak Wrap - $12.95
Turkey Meatball Fettuccini - $13.45
Chicken Alfredo - $13.45
Chicken Parmesan - $13.95
Pesto Chicken Pasta - $13.45
Steak Bite and Green Stir Fry - $13.45
Asian Chicken Teriyaki - $13.45
Please include our logo

```html
<!DOCTYPE html>
<html lang="en">
<head>
<meta charset="utf-8">
<title>Verdale Menu Board</title>
<link href="https://fonts.googleapis.com/css2?family=League+Spartan:wght@600;700;800&display=swap" rel="stylesheet">
<style>
  :root {
    --lime: #93c01f;
    --black: #000000;
    --white: #ffffff;
    --muted: #a3a3a3;
    --ink: #111111;
    --plate: #e9e9e9;
    --food-warm: #c99a62;
    --food-egg: #f1c24a;
  }
  * { margin: 0; padding: 0; box-sizing: border-box; }
  html, body { width: 1200px; height: 848px; overflow: hidden; background: var(--black); }
  .menu-board {
    position: relative;
    width: 1200px;
    height: 848px;
    background: var(--black);
    font-family: "League Spartan", "Montserrat", sans-serif;
    overflow: hidden;
  }
  .breakfast-panel {
    position: absolute;
    left: 0; top: 0;
    width: 483px; height: 703px;
    background: var(--lime);
  }
  .photo {
    position: absolute;
  }
  .photo-pancakes {
    left: 18px; top: 28px; width: 450px; height: 190px;
    border-radius: 10px 10px 40px 40px;
    background: radial-gradient(ellipse at 55% 45%, var(--food-warm) 0%, #a9764a 30%, var(--plate) 55%, #d6d6d6 100%);
  }
  .photo-omelette {
    left: 520px; top: 676px; width: 645px; height: 172px;
    border-radius: 24px 24px 0 0;
    background: linear-gradient(100deg, var(--plate) 0%, var(--food-egg) 25%, #e8a447 50%, #8a5a30 70%, var(--plate) 100%);
  }
  .section-title {
    position: absolute;
    font-weight: 700;
    letter-spacing: 1px;
    line-height: 1;
  }
  .breakfast-title {
    left: 18px; top: 282px;
    font-size: 60px;
    color: var(--ink);
  }
  .breakfast-rule {
    position: absolute;
    left: 15px; top: 346px;
    width: 444px; height: 3px;
    background: var(--ink);
  }
  .breakfast-item {
    position: absolute;
    left: 32px;
    width: 420px;
    display: flex;
    justify-content: space-between;
    font-size: 27px;
    font-weight: 700;
    line-height: 1.15;
    color: var(--ink);
  }
  .breakfast-item .price { width: 98px; }
  .lunch-title {
    left: 682px; top: 28px; width: 321px;
    text-align: center;
    font-size: 64px;
    color: var(--lime);
  }
  .lunch-rule {
    position: absolute;
    left: 682px; top: 92px;
    width: 321px; height: 3px;
    background: var(--lime);
  }
  .lunch-list {
    position: absolute;
    left: 533px; top: 140px;
    width: 620px;
    list-style: none;
  }
  .lunch-item {
    display: flex;
    justify-content: space-between;
    height: 49.9px;
    font-size: 28px;
    font-weight: 600;
    line-height: 30px;
    color: var(--white);
  }
  .lunch-item:nth-child(even) { color: var(--muted); }
  .lunch-item .price { font-weight: 700; }
  .brand {
    position: absolute;
    left: 72px; top: 732px;
    font-size: 60px;
    font-weight: 700;
    letter-spacing: 2px;
    line-height: 1;
    color: var(--muted);
  }
</style>
</head>
<body>
<main class="menu-board">
  <section class="breakfast-panel">
    <div class="photo photo-pancakes" role="img" aria-label="Photo of a stack of chocolate chip pancakes on a white plate"></div>
    <h2 class="section-title breakfast-title">BREAKFAST</h2>
    <div class="breakfast-rule"></div>
    <div class="breakfast-item" style="top:397px"><span>Protein Chocolate<br>Chip Pancakes</span><span class="price">$12.95</span></div>
    <div class="breakfast-item" style="top:505px"><span>Dawn Hustle<br>Burrito</span><span class="price">$11.95</span></div>
    <div class="breakfast-item" style="top:607px"><span>Hearty Harvest<br>Omelette</span><span class="price">$12.95</span></div>
  </section>

  <div class="brand">VERDALE</div>

  <h2 class="section-title lunch-title">LUNCH</h2>
  <div class="lunch-rule"></div>
  <ul class="lunch-list">
    <li class="lunch-item"><span>Butter Chicken</span><span class="price">$13.95</span></li>
    <li class="lunch-item"><span>Chicken Quesadilla</span><span class="price">$13.45</span></li>
    <li class="lunch-item"><span>Coconut Garlic Shrimp</span><span class="price">$15.95</span></li>
    <li class="lunch-item"><span>Goat Cheese Stuffed Chicken</span><span class="price">$14.95</span></li>
    <li class="lunch-item"><span>Chipotle Steak Wrap</span><span class="price">$12.95</span></li>
    <li class="lunch-item"><span>Turkey Meatball Fettuccini</span><span class="price">$13.45</span></li>
    <li class="lunch-item"><span>Chicken Alfredo</span><span class="price">$13.45</span></li>
    <li class="lunch-item"><span>Chicken Parmesan</span><span class="price">$13.95</span></li>
    <li class="lunch-item"><span>Pesto Chicken Pasta</span><span class="price">$13.45</span></li>
    <li class="lunch-item"><span>Steak Bite and Green Stir Fry</span><span class="price">$13.45</span></li>
    <li class="lunch-item"><span>Asian Chicken Teriyaki</span><span class="price">$13.45</span></li>
  </ul>

  <div class="photo photo-omelette" role="img" aria-label="Photo of a vegetable omelette with whole wheat toast on a white plate"></div>
</main>
</body>
</html>
```